Long term Care Provider Conference

Banner for LTC providers to know that they can rely on us to deliver high value, cost efficient, professional back office support to streamline operations, improve and maintain compliance with administrative and or nursing solutions for their agency.

Want to update the wording

```html
<!DOCTYPE html>
<html lang="en">
<head>
<meta charset="utf-8">
<title>Kestrel Care – Long-Term Care Conference Banner</title>
<link rel="stylesheet" href="https://fonts.googleapis.com/css2?family=Red+Hat+Display:wght@500;700;800&family=Inter:wght@500;600&display=swap">
<style>
  :root {
    --teal: #5f8c95;
    --teal-dark: #4f7a83;
    --teal-text: #4c8590;
    --beige: #cbbfb6;
    --ink: #2f3437;
    --ink-soft: #3f4447;
    --outline: #8d8681;
    --paper: #f8f9f9;
    --paper-grey: #eef0f1;
    --frame: #8fa7ad;
    --page: #dcdfe0;
    --photo-a: #7d7f86;
    --photo-b: #d9d6d2;
  }
  * { margin: 0; padding: 0; box-sizing: border-box; }
  html, body { width: 667px; height: 1200px; overflow: hidden; background: var(--page); }
  body { position: relative; font-family: "Inter", sans-serif; }

  .banner {
    position: absolute; left: 24px; top: 262px;
    width: 620px; height: 676px;
    background: var(--paper); overflow: hidden;
    box-shadow: 0 10px 30px rgba(0,0,0,.25);
  }
  .banner-shapes { position: absolute; inset: 0; }

  .brand {
    position: absolute; left: 55px; top: 42px;
    display: flex; align-items: center; gap: 10px;
    font-family: "Red Hat Display", sans-serif; font-weight: 800;
    font-size: 30px; color: var(--ink-soft); letter-spacing: -0.5px;
  }
  .brand-dot { width: 34px; height: 34px; border-radius: 50%; background: var(--teal); }

  .tagline {
    position: absolute; left: 305px; top: 47px; width: 300px;
    font-family: "Red Hat Display", sans-serif; font-weight: 700;
    font-size: 11.5px; letter-spacing: 1.1px; color: var(--ink);
    white-space: nowrap;
  }

  .headline {
    position: absolute; left: 54px; top: 140px;
    font-family: "Red Hat Display", sans-serif; font-weight: 800;
    font-size: 26px; line-height: 32px; color: #fff;
    white-space: nowrap;
  }

  .stats { position: absolute; left: 55px; top: 372px; width: 212px; }
  .stat { display: flex; align-items: center; height: 61px; border-bottom: 1.5px solid var(--ink-soft); }
  .stat:last-child { border-bottom: none; }
  .stat-value {
    width: 82px; flex: none; font-family: "Red Hat Display", sans-serif; font-weight: 700;
    font-size: 34px; line-height: 1;
  }
  .stat-value .digits { color: transparent; -webkit-text-stroke: 1.2px var(--outline); font-weight: 500; }
  .stat-value .unit { color: var(--ink); }
  .stat-label { font-size: 13.5px; line-height: 17px; font-weight: 500; color: var(--ink-soft); white-space: nowrap; }

  .services {
    position: absolute; left: 315px; top: 391px; width: 267px; height: 170px;
    border: 1.5px solid var(--frame); border-radius: 8px;
  }
  .services-title {
    position: absolute; left: 34px; top: -11px; padding: 0 10px;
    background: var(--paper);
    font-family: "Red Hat Display", sans-serif; font-weight: 700;
    font-size: 15px; color: var(--teal-text);
  }
  .service {
    position: absolute; display: flex; align-items: center; gap: 8px;
    font-size: 12px; line-height: 14px; font-weight: 500; color: var(--ink);
    white-space: nowrap;
  }
  .service svg { width: 20px; height: 20px; flex: none; }
  .service span { border-left: 1px solid var(--ink-soft); padding-left: 7px; }

  .web {
    position: absolute; left: 53px; top: 626px;
    font-size: 13px; font-weight: 500; color: var(--teal-text);
  }
  .contact {
    position: absolute; left: 260px; right: 0; top: 625px; text-align: center;
    font-size: 13.5px; font-weight: 500; color: #fff;
  }
  .contact .sep { margin: 0 10px; opacity: .7; }
</style>
</head>
<body>
  <main class="banner">
    <svg class="banner-shapes" viewBox="0 0 620 676" width="620" height="676">
      <defs>
        <linearGradient id="photoTone" x1="0" y1="0" x2="1" y2="1">
          <stop offset="0" stop-color="var(--photo-a)"/>
          <stop offset="1" stop-color="var(--photo-b)"/>
        </linearGradient>
      </defs>
      <rect x="0" y="590" width="620" height="86" fill="var(--paper-grey)"/>
      <polygon class="photo-underline" points="395,340 620,340 620,362 410,362" fill="var(--teal)"/>
      <g role="img" aria-label="Photo of a smiling healthcare virtual assistant wearing a headset, writing notes at her desk">
        <polygon points="330,73 620,73 620,347 300,347 300,110" fill="url(#photoTone)"/>
      </g>
      <polygon class="headline-band" points="0,112 292,112 356,217 285,328 0,328" fill="var(--teal)"/>
      <polygon points="292,112 356,217 285,328 300,328 372,217 306,112" fill="var(--teal-dark)" opacity=".55"/>
      <polygon class="stats-panel" points="0,328 224,328 296,455 224,586 0,586" fill="var(--beige)"/>
      <polygon class="footer-band" points="269,607 620,607 620,676 234,676" fill="var(--teal)"/>
    </svg>

    <div class="brand"><span class="brand-dot"></span>Kestrel Care</div>
    <p class="tagline">COMPLIANT, COST-EFFICIENT SUPPORT</p>

    <h1 class="headline">Streamline Your<br>LTC Operations<br>with Expert Back<br>Office &amp; Nursing<br>Support</h1>

    <section class="stats">
      <div class="stat"><div class="stat-value"><span class="digits">98</span><span class="unit">%</span></div><div class="stat-label">Client<br>Satisfaction</div></div>
      <div class="stat"><div class="stat-value"><span class="digits">45</span><span class="unit">k</span></div><div class="stat-label">Hours of<br>Support provided</div></div>
      <div class="stat"><div class="stat-value"><span class="digits">20</span><span class="unit">+</span></div><div class="stat-label">LTC Agencies<br>Supported</div></div>
    </section>

    <section class="services">
      <h2 class="services-title">Our Services</h2>
      <div class="service" style="left:20px;top:36px">
        <svg viewBox="0 0 20 20" fill="none" stroke="#7a8a8f" stroke-width="1.2"><circle cx="10" cy="6" r="3.5"/><path d="M3 18c0-4 3-6 7-6s7 2 7 6z"/><path d="M10 13v3M8.5 14.5h3"/></svg>
        <span>Nursing<br>Solutions</span>
      </div>
      <div class="service" style="left:20px;top:80px">
        <svg viewBox="0 0 20 20" fill="none" stroke="#7a8a8f" stroke-width="1.2"><circle cx="10" cy="10" r="3"/><circle cx="10" cy="10" r="6.5" stroke-dasharray="2.5 1.6"/></svg>
        <span>Administrative<br>Support</span>
      </div>
      <div class="service" style="left:20px;top:122px">
        <svg viewBox="0 0 20 20" fill="none" stroke="#7a8a8f" stroke-width="1.2"><rect x="3" y="2.5" width="11" height="15" rx="1"/><path d="M5.5 6.5h6M5.5 9.5h6M5.5 12.5h3"/><circle cx="15" cy="14.5" r="2.5"/></svg>
        <span>Case<br>Management</span>
      </div>
      <div class="service" style="left:150px;top:36px">
        <svg viewBox="0 0 20 20" fill="none" stroke="#7a8a8f" stroke-width="1.2"><rect x="3.5" y="2.5" width="13" height="15" rx="1"/><path d="M6 6h8M6 9h8M6 12h5"/><path d="M12 14.5h3"/></svg>
        <span>Medical<br>Billing</span>
      </div>
      <div class="service" style="left:150px;top:80px">
        <svg viewBox="0 0 20 20" fill="none" stroke="#7a8a8f" stroke-width="1.2"><path d="M10 2.5l6 2.5v5c0 4-2.7 6.5-6 7.5-3.3-1-6-3.5-6-7.5V5z"/><path d="M7 10l2 2 4-4"/></svg>
        <span>Compliance<br>Management</span>
      </div>
    </section>

    <p class="web">www.kestrelcare-va.com</p>
    <p class="contact">hello@kestrelcare-va.com<span class="sep">|</span>+1-555-014-2233</p>
  </main>
</body>
</html>
```